The name of the company is Kestrel Rehab buying foreclosed homes and remodeling

A sleek classy card. It’s a home remodel and house flip company. Something mostly black with dark gray and red in color . Something with two f”s as a logo on front as shown in pictures. Kind of just let you guys run with it . I left a few pictures that should help
You guys get an idea of what I thought was good also left all the information for back of the card

Target Market(s)

Home remodel consumers

Industry/Entity Type

Construction Company

Contact Information for Business Card

All details are on photo

Font styles to use
Decorative

Colors

Designer to choose colors to be used in the design.

Requirements
Must have
• Name of company on front. Kestrel Rehab
Nice to have
• Up to you guys I trust you
Should not have
• Not sure

```html
<!DOCTYPE html>
<html lang="en">
<head>
<meta charset="utf-8">
<title>Kestrel Rehab – Business Card</title>
<link href="https://fonts.googleapis.com/css2?family=Montserrat:wght@400;500;600;800&display=swap" rel="stylesheet">
<style>
  :root {
    --backdrop: #3a3a3c;
    --card: #060606;
    --mark-grey: #262626;
    --divider: #2e2e2e;
    --text-light: #d6d6d6;
    --accent-red: #e3141b;
  }
  * { box-sizing: border-box; margin: 0; padding: 0; }
  html, body {
    width: 1200px; height: 1000px; overflow: hidden;
    background: var(--backdrop);
    font-family: "Montserrat", sans-serif;
  }
  .canvas { position: relative; width: 1200px; height: 1000px; }
  .card {
    position: absolute; left: 220px; width: 760px; height: 430px;
    background: var(--card); border-radius: 28px;
    box-shadow: 0 18px 40px rgba(0,0,0,.45);
  }
  .card--front { top: 50px; }
  .card--back { top: 520px; }

  .front-brand {
    position: absolute; inset: 0;
    display: flex; align-items: center; justify-content: center; gap: 18px;
  }
  .brand-square { width: 34px; height: 34px; background: var(--mark-grey); }
  .brand-name {
    font-weight: 800; font-size: 54px; letter-spacing: 2px;
    color: var(--mark-grey); text-transform: uppercase;
  }

  .back-brand {
    position: absolute; left: 70px; top: 120px; width: 300px;
    display: flex; flex-direction: column; align-items: center; gap: 12px;
  }
  .back-brand .brand-name { font-size: 36px; line-height: 1.05; text-align: center; }
  .divider {
    position: absolute; left: 400px; top: 95px; width: 2px; height: 190px;
    background: var(--divider);
  }
  .contact { position: absolute; left: 430px; top: 100px; }
  .contact-name {
    color: var(--accent-red); font-weight: 600; font-size: 24px; margin-bottom: 14px;
  }
  .contact-list { list-style: none; }
  .contact-item {
    display: flex; align-items: center; gap: 12px;
    color: var(--text-light); font-size: 20px; font-weight: 500;
    line-height: 1; margin-bottom: 11px;
  }
  .contact-item svg { width: 16px; height: 16px; flex: none; }
  .web-domain { color: var(--accent-red); }

  .services {
    position: absolute; left: 0; right: 0; bottom: 50px;
    display: flex; justify-content: center; align-items: center; gap: 14px;
    color: var(--text-light); font-size: 16px; font-weight: 500; letter-spacing: .5px;
  }
  .services .bullet { width: 8px; height: 8px; background: var(--accent-red); }
</style>
</head>
<body>
<main class="canvas">
  <section class="card card--front" aria-label="Card front">
    <div class="front-brand">
      <span class="brand-square"></span>
      <span class="brand-name">Kestrel Rehab</span>
    </div>
  </section>

  <section class="card card--back" aria-label="Card back">
    <div class="back-brand">
      <span class="brand-square"></span>
      <span class="brand-name">Kestrel Rehab</span>
    </div>
    <div class="divider"></div>
    <div class="contact">
      <p class="contact-name">Daniel Whitcombe JR.</p>
      <ul class="contact-list">
        <li class="contact-item">
          <svg viewBox="0 0 24 24" fill="var(--accent-red)"><path d="M6.6 10.8a15.1 15.1 0 0 0 6.6 6.6l2.2-2.2a1 1 0 0 1 1-.25 11.4 11.4 0 0 0 3.6.57 1 1 0 0 1 1 1V20a1 1 0 0 1-1 1A17 17 0 0 1 3 4a1 1 0 0 1 1-1h3.5a1 1 0 0 1 1 1c0 1.25.2 2.45.57 3.57a1 1 0 0 1-.25 1z"/></svg>
          <span>555-012-4478</span>
        </li>
        <li class="contact-item">
          <svg viewBox="0 0 24 24" fill="var(--accent-red)"><path d="M2 5h20v14H2z"/><path d="M2 5l10 8 10-8" fill="none" stroke="var(--card)" stroke-width="2"/></svg>
          <span>whitcombejr@com</span>
        </li>
        <li class="contact-item">
          <svg viewBox="0 0 24 24" fill="none" stroke="var(--accent-red)" stroke-width="2"><circle cx="12" cy="12" r="10"/><path d="M2 12h20M12 2c3 3 3 17 0 20M12 2c-3 3-3 17 0 20"/></svg>
          <span>www.<span class="web-domain">kestrelrehab</span>.com</span>
        </li>
        <li class="contact-item">
          <svg viewBox="0 0 24 24"><circle cx="12" cy="12" r="9" fill="var(--accent-red)"/></svg>
          <span>kestrel_rehab</span>
        </li>
      </ul>
    </div>
    <div class="services">
      <span>GENERAL GONTRACTOR</span><span class="bullet"></span>
      <span>HOME REMODEL</span><span class="bullet"></span>
      <span>CONCRETE ALTENITIUS</span>
    </div>
  </section>
</main>
</body>
</html>
```